Harlowe Products - Plumbing Consumables and Equipment Catalog

Background Information:
Harlowe Products, an expert in the plumbing equipment industry for over two decades, connects leading manufacturers worldwide with premier American plumbing contractors. We specialize in high-performance and sustainable solutions for both residential and commercial plumbing needs.

Design Requirements:
We are seeking a catalogue that captures the high quality and technical sophistication of our equipment and consumables:

Professional layout incorporating our brand colors and logo.
High-quality images and detailed descriptions for our products including UV systems, robotic cutters, and inspection cameras.
Special emphasis on our consumable products like liners, calibration tubes, resin, spot repair kits, fiber glass rolls, and T-wraps.
Organized sections by product category, highlighting key equipment and consumables for easy reference.
Inclusion of detailed product specifications, usage instructions, and compatibility information for consumables.
Contact information and social media links for customer engagement.

Selection Criteria:
Proven track record in technical or industrial product catalogue design.
Clarity and precision in the presentation of both durable equipment and consumable products.

PLEASE DO NOT USE ANY LOGO THAT SAYS OKV!!!

All Product Photo s will be sent in a zip file to e-mail address!
Website: harloweproducts-demo.us

Please feel free to reach out for more information or to brainstorm ideas. Thank you!

Designs look the same

Target Market(s)

Plumbers

Industry/Entity Type

Trenchless Technology

Colors
0054AA
0677BA
7BADD7
CADEEF
E8F1F8
EB3D1F
EC4F4E
F09395
F8D3D4
FCEDEE

Requirements
Must have
• We are seeking a catalogue that captures the high quality and technical sophistication of our equipment and consumables: Professional layout incorporating our brand colors and logo. High-quality images and detailed descriptions for our products including UV systems, robotic cutters, and inspection cameras. Special emphasis on our consumable products like liners, calibration tubes, resin, spot repair kits, fiber glass rolls, and T-wraps. Organized sections by product category, highlighting key equipment and consumables for easy reference. Inclusion of detailed product specifications, usage instructions, and compatibility information for consumables. Contact information and social media links for customer engagement.
Nice to have
• Please feel free to reach out for more information or to brainstorm ideas. Thank you!

```html
<!DOCTYPE html>
<html lang="en">
<head>
<meta charset="utf-8">
<title>Harlowe Products – 2024 Catalog</title>
<link rel="stylesheet" href="https://fonts.googleapis.com/css2?family=Audiowide&family=Open+Sans:wght@400;600;700&display=swap">
<style>
:root{
  --brand-blue:#1f3a95;
  --brand-red:#e8202a;
  --tint:#e8ecf6;
  --grey:#cfcfcf;
  --ink:#1b1b1b;
  --white:#ffffff;
  --line:#d9dbe3;
}
*{box-sizing:border-box;margin:0;padding:0}
html,body{width:868px;height:1200px;overflow:hidden;background:var(--white)}
body{font-family:"Open Sans",Arial,sans-serif;color:var(--ink)}
.canvas{position:relative;width:868px;height:1200px;overflow:hidden;background:var(--white)}
.page{position:absolute;width:402px;height:568px;background:var(--white);overflow:hidden;box-shadow:0 0 6px rgba(0,0,0,.12)}
.page--cover{left:23px;top:24px}
.page--index{left:443px;top:24px}
.page--products{left:23px;top:609px}
.page--category{left:443px;top:609px}
.abs{position:absolute}
.display{font-family:"Audiowide",sans-serif}

/* brand mark */
.brand{position:absolute;display:flex;align-items:center;gap:4px;color:var(--brand-blue);font-family:"Open Sans",sans-serif;font-weight:700;white-space:nowrap}
.brand__dot{border-radius:50%;background:var(--brand-blue)}
.brand--large{left:38px;top:34px;font-size:13px}
.brand--large .brand__dot{width:16px;height:16px}
.brand--small{right:24px;top:26px;font-size:6.5px}
.brand--small .brand__dot{width:8px;height:8px}

/* cover */
.cover__bar{left:354px;top:0;width:16px;height:88px;background:var(--brand-red)}
.cover__photo{left:24px;top:86px;width:353px;height:274px;background:linear-gradient(180deg,#5b5d63 0%,#7b6f6a 45%,#3c4156 100%)}
.cover__grey{left:318px;top:358px;width:85px;height:38px;background:var(--grey)}
.cover__panel{left:0;top:284px;width:317px;height:171px;background:rgba(31,58,149,.93)}
.cover__year{left:37px;top:318px;color:var(--white);font-size:12px}
.cover__title{left:38px;top:342px;color:var(--white);font-size:29px;line-height:40px;text-shadow:2px 2px 0 var(--brand-red)}
.cover__tagline{left:39px;top:472px;width:260px;font-size:9.6px;line-height:17.5px}
.cover__tagline strong{font-weight:600}

/* index */
.index__title{left:40px;top:64px;font-size:29px;color:var(--brand-blue)}
.index__block{left:24px;top:140px;width:123px;height:379px;background:var(--brand-blue)}
.index__frame{left:69px;top:158px;width:77px;height:327px;border:1px solid var(--white)}
.index__bracket{left:146px;top:158px;width:18px;height:327px;border:1px solid var(--brand-red);border-left:none}
.index__list{list-style:none;position:absolute;left:0;top:177px;width:402px}
.index__list li{position:relative;height:29.7px;font-size:12px;line-height:18px}
.index__num{position:absolute;left:96px;color:var(--white);font-weight:700}
.index__tick{position:absolute;left:163px;top:9px;width:3px;height:1.5px;background:var(--brand-red)}
.index__label{position:absolute;left:184px;color:var(--ink)}
.index__grey{left:184px;top:531px;width:218px;height:38px;background:var(--grey)}

/* product pages */
.section-title{position:absolute;left:25px;font-family:"Audiowide",sans-serif;font-size:16.5px;color:var(--brand-blue);letter-spacing:.3px;line-height:20px}
.tint{position:absolute;background:var(--tint)}
.tile{position:absolute;width:107px;height:83px;border:1px solid var(--line);background:var(--white)}
.tile__art{position:absolute;inset:6px}
.caption{position:absolute;width:122px;text-align:center;font-size:9.5px;line-height:13px}
.caption__name{font-family:"Audiowide",sans-serif;color:var(--brand-red);font-size:9.5px;line-height:13px}
.caption__meta{margin-top:4px;font-size:9.5px;line-height:17px;color:var(--ink)}

/* category */
.circle{position:absolute;top:80px;width:98px;height:98px;border-radius:50%;background:var(--brand-blue);color:var(--white);display:flex;align-items:center;justify-content:center;text-align:center;font-family:"Audiowide",sans-serif;font-size:9px;line-height:14px}
.spec__body{left:25px;top:278px;width:210px;font-size:9.8px;line-height:16.9px}
.spec__body p+p{margin-top:3px}
.spec__photo{left:250px;top:220px;width:152px;height:187px;background:linear-gradient(160deg,#6b6356 0%,#b7b3ad 45%,#4e4a46 100%)}
.spec__bar{left:365px;top:390px;width:11px;height:36px;background:var(--brand-red)}
.footer{left:0;top:434px;width:317px;height:134px;background:var(--brand-blue);color:var(--white)}
.footer__grey{left:317px;top:434px;width:85px;height:134px;background:#b9b9b9}
.office{position:absolute;top:22px;font-size:7.6px;line-height:12px}
.office h3{font-size:8.4px;font-weight:600;margin-bottom:9px}
.office p{margin-bottom:5px}
.social{position:absolute;left:351px;width:16px;height:16px;border:1px solid var(--brand-blue);border-radius:50%}
</style>
</head>
<body>
<div class="canvas">

  <!-- Cover -->
  <section class="page page--cover">
    <div class="abs cover__bar"></div>
    <div class="brand brand--large"><span class="brand__dot"></span>Harlowe Products</div>
    <div class="abs cover__photo" role="img" aria-label="Team of five staff standing in a warehouse behind pipe-lining machines and equipment"></div>
    <div class="abs cover__grey"></div>
    <div class="abs cover__panel"></div>
    <div class="abs cover__year">2024</div>
    <h1 class="abs display cover__title">HARLOWE<br>PRODUCTS</h1>
    <p class="abs cover__tagline">Connecting the world’s top plumbing equipment manufacturers with <strong>America’s leading plumbing contractors—global unity, local service</strong></p>
  </section>

  <!-- Index -->
  <section class="page page--index">
    <div class="brand brand--small"><span class="brand__dot"></span>Harlowe Products</div>
    <h2 class="abs display index__title">INDEX</h2>
    <div class="abs index__block"></div>
    <div class="abs index__frame"></div>
    <div class="abs index__bracket"></div>
    <ol class="index__list">
      <li><span class="index__num">1.</span><span class="index__tick"></span><span class="index__label">About Harlowe Products</span></li>
      <li><span class="index__num">2.</span><span class="index__tick"></span><span class="index__label">Liners</span></li>
      <li><span class="index__num">3.</span><span class="index__tick"></span><span class="index__label">Glass Matting</span></li>
      <li><span class="index__num">4.</span><span class="index__tick"></span><span class="index__label">Cal Tube</span></li>
      <li><span class="index__num">5.</span><span class="index__tick"></span><span class="index__label">T-Wrap</span></li>
      <li><span class="index__num">6.</span><span class="index__tick"></span><span class="index__label">Epoxy Resin</span></li>
      <li><span class="index__num">7.</span><span class="index__tick"></span><span class="index__label">UV Resin</span></li>
      <li><span class="index__num">8.</span><span class="index__tick"></span><span class="index__label">Silicate Resin</span></li>
      <li><span class="index__num">9.</span><span class="index__tick"></span><span class="index__label">Equipment</span></li>
      <li><span class="index__num">10.</span><span class="index__tick"></span><span class="index__label">Contact US</span></li>
    </ol>
    <div class="abs index__grey"></div>
  </section>

  <!-- Products -->
  <section class="page page--products">
    <div class="tint" style="left:0;top:61px;width:40px;height:64px"></div>
    <h2 class="section-title" style="top:21px">OUR PRODUCTS</h2>
    <div class="brand brand--small"><span class="brand__dot"></span>Harlowe Products</div>

    <div class="tile" style="left:24px;top:78px"><div class="tile__art" role="img" aria-label="UV curing system cart with light train" style="background:linear-gradient(180deg,#eef1f4,#bfe3f3)"></div></div>
    <div class="tile" style="left:146px;top:78px"><div class="tile__art" role="img" aria-label="Robotic cutter control unit with red hose" style="background:linear-gradient(180deg,#f1f1f1,#c9c9cc)"></div></div>
    <div class="tile" style="left:269px;top:78px"><div class="tile__art" role="img" aria-label="Inspection camera reel on stand" style="background:linear-gradient(180deg,#eef3f8,#8fb4dc)"></div></div>

    <div class="caption" style="left:17px;top:163px"><div class="caption__name">UV SYSTEM</div><div class="caption__meta">BrightCure+<br>Price$999,999.00</div></div>
    <div class="caption" style="left:139px;top:163px"><div class="caption__name">ROBOTIC CUTTER</div><div class="caption__meta">Vantor - ClimbMax E<br>Price$86,575.82</div></div>
    <div class="caption" style="left:262px;top:163px"><div class="caption__name">INSPECTION<br>CAMERAS</div><div class="caption__meta" style="margin-top:2px">Orbit with Rotary</div></div>

    <div class="tint" style="left:312px;top:253px;width:90px;height:64px"></div>
    <h2 class="section-title" style="top:246px">CONSUMABLE PRODUCTS</h2>

    <div class="tile" style="left:24px;top:298px"><div class="tile__art" role="img" aria-label="Rolled white liner" style="background:radial-gradient(circle,#ffffff 30%,#e4e4e4 75%)"></div></div>
    <div class="tile" style="left:146px;top:298px"><div class="tile__art" role="img" aria-label="Coloured calibration tube rolls" style="background:linear-gradient(135deg,#3a56b5,#8a6fd0 50%,#f0602e)"></div></div>
    <div class="tile" style="left:269px;top:298px"><div class="tile__art" role="img" aria-label="Black resin container" style="background:radial-gradient(circle,#2a2a2a 38%,#ffffff 40%)"></div></div>

    <div class="caption" style="left:17px;top:389px"><div class="caption__name">LINERS</div></div>
    <div class="caption" style="left:139px;top:389px"><div class="caption__name">CALIBRATION<br>TUBES</div></div>
    <div class="caption" style="left:262px;top:389px"><div class="caption__name">RESIN</div></div>

    <div class="tile" style="left:24px;top:429px"><div class="tile__art" role="img" aria-label="Spot repair kit illustration" style="background:linear-gradient(180deg,#ffffff,#dfe7f4)"></div></div>
    <div class="tile" style="left:146px;top:429px"><div class="tile__art" role="img" aria-label="Fiberglass roll close-up" style="background:linear-gradient(180deg,#f7f7f7,#e2e2e2)"></div></div>
    <div class="tile" style="left:269px;top:429px"><div class="tile__art" role="img" aria-label="Purple T-wrap roll" style="background:radial-gradient(circle,#8b86d8 35%,#ffffff 62%)"></div></div>

    <div class="caption" style="left:17px;top:519px"><div class="caption__name">SPOT REPAIR KITS</div></div>
    <div class="caption" style="left:139px;top:519px"><div class="caption__name">FIBERGLASS ROLLS</div></div>
    <div class="caption" style="left:262px;top:519px"><div class="caption__name">T-WRAPS</div></div>
  </section>

  <!-- Category -->
  <section class="page page--category">
    <div class="tint" style="left:0;top:61px;width:92px;height:64px"></div>
    <h2 class="section-title" style="top:21px">PRODUCT CATEGORY</h2>
    <div class="brand brand--small"><span class="brand__dot"></span>Harlowe Products</div>

    <div class="circle" style="left:25px">DRAIN<br>CLEANING</div>
    <div class="circle" style="left:151px">MATERIALS</div>
    <div class="circle" style="left:278px">EQUIPMENT</div>

    <div class="tint" style="left:0;top:240px;width:30px;height:45px"></div>
    <h2 class="section-title" style="top:232px;line-height:22px">PRODUCT<br>SPECIFICATIONS</h2>
    <div class="abs spec__body">
      <p>Lorem ipsum dolor sit aonsecte adipiscing elit, sed do eiusmod tempor incididunt ut labore et dolore magna aliqua. Quis ipsum suspendisse ultrices grava. Risus commodo vivra maecenas accumsan lacus.</p>
      <p>Lorem ipsum dolor sit aonsecte adipiscing elit, sed do eiusmod tempor incididunt.</p>
    </div>
    <div class="abs spec__photo" role="img" aria-label="Three staff members holding up printed posters in a workshop"></div>
    <div class="abs spec__bar"></div>

    <footer class="abs footer">
      <div class="office" style="left:24px">
        <h3>West Coast</h3>
        <p>418 Alder Crest Way<br>Seabrook, C.A. 92000</p>
        <p>555-010-4821</p>
        <p>info@harloweproducts-demo.us</p>
      </div>
      <div class="office" style="left:156px">
        <h3>Main Office</h3>
        <p>27 Linden Hill Rd<br>Maple Ford, N.J. 07000</p>
        <p>555-010-7734</p>
        <p>info@harloweproducts-demo.us</p>
      </div>
    </footer>
    <div class="abs footer__grey"></div>
    <span class="social" style="top:466px" aria-label="Social link"></span>
    <span class="social" style="top:492px" aria-label="Social link"></span>
    <span class="social" style="top:519px" aria-label="Social link"></span>
  </section>

</div>
</body>
</html>
```